DL Flyer Lantern Creek Hotel Thursday Night Bonus

We require a DL Portrait and landscape flyer for our Thursday Night Bonus Pull.
The way the draw works you must be part of our loyalty program, and on a Thursday night anytime between 5pm and 7pm, a name/number will be picked at random. If that person is in the hotel at the time they will win the jackpot.

The jackpot starts at $250 and goes up by $50 each week, if not won.

The things that the flyer must state:-
* loyalty program members only
* drawn on a Thursday night anytime between 5pm and 7pm
* QMRV/58/46271 must be written somewhere.
* see staff for details.
* our logo

Would like the flyer to be catch peoples attention but remain professional

If your unable to download logo, please forward email address and I will send it throuh

```html
<!DOCTYPE html>
<html lang="en">
<head>
<meta charset="utf-8">
<title>Thursday Night Bonus Pull — Lantern Creek Hotel</title>
<link href="https://fonts.googleapis.com/css2?family=Cinzel:wght@400;600&family=Dancing+Script:wght@600;700&display=swap" rel="stylesheet">
<style>
  :root {
    --night: #111111;
    --night-mid: #262626;
    --gold-deep: #a87425;
    --gold: #c9953f;
    --gold-light: #f2e0a4;
    --cream: #fbf6e4;
    --ink: #1e1a14;
    --white: #ffffff;
  }
  html, body {
    margin: 0;
    padding: 0;
    width: 1200px;
    height: 846px;
    overflow: hidden;
    background: var(--white);
  }
  .flyer {
    position: relative;
    width: 1200px;
    height: 846px;
    overflow: hidden;
    background:
      repeating-linear-gradient(90deg, rgba(255,255,255,0.025) 0 2px, transparent 2px 7px),
      linear-gradient(180deg, var(--night) 0%, var(--night-mid) 45%, var(--night) 80%);
    font-family: "Cinzel", "Times New Roman", serif;
  }
  .balls-left, .balls-right {
    position: absolute;
  }
  .balls-left { left: 0; top: 0; width: 470px; height: 410px; }
  .balls-right { left: 870px; top: 180px; width: 330px; height: 290px; }

  .script {
    font-family: "Dancing Script", cursive;
    font-weight: 700;
    color: var(--gold);
    background: linear-gradient(90deg, var(--gold-deep), var(--gold-light) 60%, var(--gold));
    -webkit-background-clip: text;
    background-clip: text;
    -webkit-text-fill-color: transparent;
  }
  .title-script {
    position: absolute;
    left: 348px;
    top: 78px;
    margin: 0;
    font-size: 66px;
    line-height: 1;
  }
  .title-word {
    position: absolute;
    left: 325px;
    top: 167px;
    margin: 0;
    display: flex;
    gap: 3px;
  }
  .title-letter {
    width: 78px;
    height: 78px;
    border: 1.5px solid var(--gold);
    border-radius: 50%;
    display: flex;
    align-items: center;
    justify-content: center;
    color: var(--white);
    font-size: 52px;
    font-weight: 400;
    line-height: 1;
  }
  .title-tail {
    position: absolute;
    left: 780px;
    top: 196px;
    margin: 0;
    font-size: 42px;
    font-weight: 400;
    color: var(--gold);
    letter-spacing: 1px;
  }

  .draw-time {
    position: absolute;
    left: 87px;
    top: 424px;
    width: 480px;
  }
  .draw-time .script {
    display: block;
    font-size: 37px;
    line-height: 1.1;
  }
  .draw-time p {
    margin: 6px 0 0;
    color: var(--white);
    font-size: 21px;
    line-height: 32px;
    letter-spacing: 0.5px;
  }

  .pill {
    position: absolute;
    left: 617px;
    width: 480px;
    box-sizing: border-box;
    border-radius: 15px;
    background: linear-gradient(90deg, var(--gold-deep) 0%, var(--gold) 35%, var(--gold-light) 80%, var(--cream) 100%);
    color: var(--ink);
    padding: 0 20px;
    font-size: 19.5px;
    letter-spacing: 0.4px;
    display: flex;
    flex-direction: column;
    justify-content: center;
  }
  .pill-jackpot { top: 455px; height: 75px; line-height: 27px; }
  .pill-members { top: 549px; height: 53px; }
  .pill strong { font-size: 23px; font-weight: 600; }

  .wave {
    position: absolute;
    left: 0;
    top: 560px;
    width: 1200px;
    height: 286px;
  }

  .hotel-name {
    position: absolute;
    left: 88px;
    top: 724px;
    display: flex;
    align-items: center;
    gap: 18px;
    color: var(--ink);
    font-size: 44px;
    font-weight: 400;
    line-height: 1;
  }
  .hotel-name .mark {
    width: 74px;
    height: 74px;
    border-radius: 50%;
    background: var(--gold);
  }
  .hotel-name span { display: block; }

  .fine-print {
    position: absolute;
    left: 927px;
    top: 755px;
    margin: 0;
    color: var(--gold);
    font-size: 15px;
    line-height: 21px;
    letter-spacing: 0.3px;
  }
</style>
</head>
<body>
  <main class="flyer">
    <svg class="balls-left" role="img" aria-label="White lottery balls carrying the hotel name and the bonus pull title" viewBox="0 0 470 410">
      <defs>
        <radialGradient id="pearl" cx="45%" cy="38%" r="65%">
          <stop offset="0%" stop-color="#ffffff"/>
          <stop offset="70%" stop-color="#e8e8e6"/>
          <stop offset="100%" stop-color="#9c9c98"/>
        </radialGradient>
      </defs>
      <circle cx="245" cy="300" r="108" fill="url(#pearl)"/>
      <circle cx="405" cy="330" r="60" fill="url(#pearl)"/>
      <circle cx="133" cy="150" r="150" fill="url(#pearl)"/>
    </svg>

    <svg class="balls-right" role="img" aria-label="Gold lottery balls marked add up fifty dollars each week and win two hundred fifty dollars" viewBox="0 0 330 290">
      <defs>
        <radialGradient id="goldball" cx="50%" cy="45%" r="60%">
          <stop offset="0%" stop-color="#fffbe8"/>
          <stop offset="60%" stop-color="#f1de9e"/>
          <stop offset="100%" stop-color="#b58a3a"/>
        </radialGradient>
      </defs>
      <circle cx="272" cy="48" r="45" fill="#0a0a0a"/>
      <circle cx="290" cy="240" r="48" fill="#0a0a0a"/>
      <circle cx="225" cy="148" r="95" fill="url(#goldball)"/>
      <circle cx="103" cy="185" r="73" fill="url(#goldball)"/>
    </svg>

    <h1 class="title">
      <span class="title-script script">Thursday Night</span>
      <span class="title-word">
        <span class="title-letter">B</span>
        <span class="title-letter">O</span>
        <span class="title-letter">N</span>
        <span class="title-letter">U</span>
        <span class="title-letter">S</span>
      </span>
      <span class="title-tail">PULL</span>
    </h1>

    <section class="draw-time">
      <span class="script">Drawn on a Thursday night</span>
      <p>WIN THE JACKPOT IF YOU ARE IN<br>THE HOTEL ANYTIME BETWEEN<br>5PM AND 7PM</p>
    </section>

    <div class="pill pill-jackpot">
      <span>THE JACKPOT STARTS AT <strong>$250</strong></span>
      <span>AND GOES UP BY <strong>$50</strong> EACH WEEK</span>
    </div>
    <div class="pill pill-members">LOYALTY PROGRAM MEMBERS ONLY</div>

    <svg class="wave" viewBox="0 0 1200 286" preserveAspectRatio="none" aria-hidden="true">
      <defs>
        <linearGradient id="band" x1="0" y1="0" x2="1" y2="0">
          <stop offset="0%" stop-color="#a87425"/>
          <stop offset="40%" stop-color="#dcb266"/>
          <stop offset="75%" stop-color="#c9953f"/>
          <stop offset="100%" stop-color="#a87425"/>
        </linearGradient>
      </defs>
      <path d="M0 70 C 180 40, 330 20, 470 25 C 680 32, 900 80, 1200 75 L1200 286 L0 286 Z" fill="url(#band)"/>
      <path d="M0 118 C 200 125, 380 158, 560 150 C 780 140, 1000 95, 1200 78 L1200 286 L0 286 Z" fill="#ffffff"/>
    </svg>

    <div class="hotel-name">
      <div class="mark"></div>
      <div><span>LANTERN CREEK</span><span>HOTEL</span></div>
    </div>

    <p class="fine-print">SEE STAFF FOR DETAILS<br>QMRV/58/46271</p>
  </main>
</body>
</html>
```